Web Design Home Page

KRVL Athletics.com – Homepage Vision
KRVL is a community based youth sports program currently running basketball and soccer programs. We run recreational leagues, competitive club programs and run many camps, clinics and development programs in both sports.
My vision on the KRVL Home page was to design a clean page that will guide viewers quickly to the sport of interest.
At the top I was thinking of a KRVL Logo Bar. I want something that we can also customize for each of the sports to use in the future. So, 5 different logo bars.
1 – KRVL Athletics Logo Bar – Goes on the KRVLAthletics.com home page, which give general information about the club as a whole and leads folks to the sport they want to go.
2 – KRVL Basketball – Recreational. Same look as the homepage logo bar but only contains info regarding to recreational basketball.
3 – KRVL Basketball – Competitive. Same as above but only competitive basketball.
4 – KRVL Soccer – Recreational. Same as above but only recreational soccer.
5 – KRVL Soccer – Competitive. Same as above but only competitive soccer.
Maybe the logo bar on the home page can also be the main logo bar and also rotate the other 4 underneath the main logo bar. Logo are old, may need to be updated at some point.
The middle section, I was thinking of 4 boxes that when clicked on will take you to the appropriate website. The designs I used are just to show something. I took the picture off the web and they may be copyrighted so would probably need some type of original designs.
Recreational Basketball Website - http://krvlathletics-example.com/basketball/index.html
Competitive Basketball Website - http://www.krvlherons-example.com/
Recreational Soccer Website - http://krvlathletics-example.com/soccer/index.html
Competitive Soccer Website - http://www.ridgepremiersoccer-example.com/
Recreational basketball uses Granite Mesa Basketball (we own the trade name) or KRVL Basketball.
The competitive basketball club is known as KRVL Herons.
Recreational soccer goes by Granite Mesa Soccer or Granite Mesa Soccer Club.
Competitive soccer goes by Ridge Premier Soccer or Granite Mesa Soccer Club.
Then on the bottom of the page I was thinking of a menus bar that contains information general to the club (both basketball and soccer). When you click on any a pop up box will pop up with the information for each listed below.
About Us
Granite Mesa Athletic Club provides recreational leagues for both Basketball and Soccer with the focus placed on providing our youth with the rewarding opportunity of participating in youth sports. Our direction is to promote the recreational value of youth sports while emphasizing fun and respect for the sport.
Granite Mesa Athletic Club (KRVL) is based in the North Phoenix area with most of our players residing in the Willow Bend School District.
Our Mission
Our mission at Granite Mesa Athletic Club is to promote and develop excellence in youth sports based on skill, sportsmanship, values, and player character. Our programs aim to provide an environment for natural player development that prepares them for life experiences, both on and off the field.
We focus on a uniform sports philosophy throughout the club that emphasizes growth through positive reinforcement resulting in players achieving his/her fullest potential. We do not look for the next victory to measure our success, but in the total learning experience for each player, realizing that the team is much stronger than an individual.
Contact Info
Granite Mesa Athletic Club
P.O. Box 7068
Willow Bend, AZ 85990
Club Phone – 480-555-0173
Club Website – KRVLAthletics.com
Club Email – info@krvlathletics-example.com
Basketball Email – KRVLBB@mail-example.com
Soccer Email – KRVLSoccer@mail-example.com
Our Mission
The mission of KRVL shall be to promote good citizenship and health through community athletic activities for children and for educational purposes. Club focus is on player development, with emphasis on teamwork and sportsmanship with high standards for both parents and players. Respect, commitment and accountability are qualities we ask all our members to endorse both on and off the field.

```html
<!DOCTYPE html>
<html lang="en">
<head>
<meta charset="utf-8">
<title>Player Expectations – KRVL Athletics</title>
<link rel="stylesheet" href="https://fonts.googleapis.com/css2?family=Audiowide&family=Open+Sans:wght@600;700&display=swap">
<style>
  :root {
    --wall: #d9d9d6;
    --wall-light: #ececea;
    --wall-dark: #c4c4c1;
    --green-dark: #4a6531;
    --green: #587a3c;
    --green-mid: #6b8a4c;
    --green-soft: #8fa875;
    --tile: #8aab6d;
    --tile-edge: #b9cda6;
    --white: #ffffff;
    --shadow: rgba(0, 0, 0, 0.35);
  }
  * { box-sizing: border-box; margin: 0; padding: 0; }
  html, body { width: 1200px; height: 675px; overflow: hidden; }
  body {
    position: relative;
    font-family: "Open Sans", Arial, sans-serif;
    color: var(--white);
    background:
      radial-gradient(ellipse at 30% 40%, var(--wall-light), transparent 60%),
      radial-gradient(ellipse at 80% 80%, var(--wall-dark), transparent 55%),
      var(--wall);
  }
  a { color: inherit; text-decoration: none; }

  /* Logo bar */
  .logo-bar {
    position: absolute; left: 5px; top: 40px; width: 1190px; height: 48px;
    background: linear-gradient(to bottom, var(--green-mid), var(--green) 40%, var(--green-dark));
    border-radius: 4px;
    box-shadow: 0 3px 5px var(--shadow);
  }
  .page-title {
    position: absolute; left: 590px; top: 50px;
    font-family: "Audiowide", "Arial Black", sans-serif;
    font-size: 29px; font-weight: 400; line-height: 36px;
    text-shadow: 1px 1px 2px rgba(0, 0, 0, 0.3);
  }

  /* Side navigation */
  .side-nav {
    position: absolute; left: 296px; top: 86px; width: 105px; height: 452px;
    background: linear-gradient(to bottom, var(--green), var(--green-dark));
    box-shadow: 2px 3px 6px var(--shadow);
  }
  .club-mark {
    position: absolute; left: 313px; top: 48px; width: 70px; height: 70px;
    border: 3px solid var(--white); border-radius: 50%;
    background: var(--green);
  }
  .club-name {
    position: absolute; left: 296px; top: 117px; width: 105px;
    text-align: center; font-size: 13px; font-weight: 700; letter-spacing: 1px;
  }
  .nav-list {
    position: absolute; left: 296px; top: 140px; width: 105px; list-style: none;
  }
  .nav-list li {
    height: 37.4px; line-height: 28px; margin: 0 3px;
    text-align: center; font-size: 8.5px; font-weight: 700;
  }
  .nav-list li.is-current { background: rgba(255, 255, 255, 0.08); line-height: 29px; }

  /* Sport boxes */
  .sport-tile {
    position: absolute; left: 231px; width: 61px; height: 61px;
    background: var(--tile);
    border: 2px solid var(--tile-edge);
    box-shadow: 2px 3px 4px var(--shadow);
  }
  .sport-tile .ball {
    position: absolute; left: 5px; top: 5px; width: 47px; height: 47px;
    border: 3px solid var(--white); border-radius: 50%;
  }
  .sport-tile .level {
    position: absolute; right: 4px; bottom: 2px; font-size: 8px; font-weight: 700;
  }

  /* Content */
  .content-panel {
    position: absolute; left: 418px; top: 88px; width: 539px; height: 450px;
    background: linear-gradient(to bottom, #93ab79, var(--green-soft));
    box-shadow: 2px 3px 6px var(--shadow);
    padding: 37px 76px 0 62px;
  }
  .content-panel p {
    font-size: 10.6px; font-weight: 600; line-height: 13px; margin-bottom: 14px;
  }

  /* Club menu bar */
  .footer-bar {
    position: absolute; left: 211px; top: 545px; width: 765px; height: 35px;
    background: linear-gradient(to bottom, var(--green-mid), var(--green-dark));
    border-radius: 4px;
    box-shadow: 0 3px 5px var(--shadow);
  }
  .social-links {
    position: absolute; right: 34px; top: 0; height: 35px;
    display: flex; gap: 14px; align-items: center;
    font-size: 10px; font-weight: 700; list-style: none;
  }
</style>
</head>
<body>
  <header class="logo-bar"></header>
  <h1 class="page-title">Player Expectations</h1>

  <nav class="side-nav" aria-label="Main"></nav>
  <div class="club-mark" aria-hidden="true"></div>
  <div class="club-name">KRVL</div>
  <ul class="nav-list">
    <li>Announcement</li>
    <li>Teams</li>
    <li class="is-current">Player Expectations</li>
    <li>Try outs</li>
    <li>Training Staff</li>
    <li>FAQ</li>
    <li>Contact us</li>
  </ul>

  <a class="sport-tile" style="top:111px" href="http://krvlathletics-example.com/basketball/index.html" aria-label="KRVL Basketball – Recreational"><span class="ball"></span><span class="level">R</span></a>
  <a class="sport-tile" style="top:203px" href="http://www.krvlherons-example.com/" aria-label="KRVL Herons – Competitive basketball"><span class="ball"></span><span class="level">C</span></a>
  <a class="sport-tile" style="top:296px" href="http://krvlathletics-example.com/soccer/index.html" aria-label="KRVL Soccer – Recreational"><span class="ball"></span><span class="level">R</span></a>
  <a class="sport-tile" style="top:391px" href="http://www.ridgepremiersoccer-example.com/" aria-label="Ridge Premier Soccer – Competitive"><span class="ball"></span><span class="level">C</span></a>

  <main class="content-panel">
    <p>Be ready to practice promptly at our start times. If needed, show up a few minutes early to get yourself ready.</p>
    <p>Please be at the games at least 20 minutes prior to the game start.</p>
    <p>If you have to miss a practice, game, or are going to be late, please let your coach know in advance. A commitment to attend all possible training sessions and games is expected.</p>
    <p>Excel in the classroom. You will either pay the price now, or you'll pay a bigger price later! If you can't pass, you can't play.</p>
    <p>Respect of coaches, players and referees is expected at all times. Breaking of this rule will result in consequences determined by the KRVL Director. Players are to listen and concentrate on what the coach says at all times.</p>
    <p>Players must also be able to accept constructive criticism without excuses.</p>
    <p>Players are to always do their best in practice and games to improve upon their level of play. We play as we practice; always give 100% when on the floor.</p>
    <p>Players must always put the team first. A player must accept decisions that are made for the good of the team.</p>
    <p>Never Give Up! Winners never quit and quitters never win.</p>
    <p>Represent the KRVL program appropriately on the court, in the classroom, and in the community.</p>
  </main>

  <footer class="footer-bar">
    <ul class="social-links">
      <li>Pagebook</li>
      <li>Chirper</li>
    </ul>
  </footer>
</body>
</html>
```